bramblegate crest roofing flyer*

I need an a5 size flyer designing to go in our local advertising magazine.We are based in the north west of England Id like key features from the website including on the flyer, possibly even reviews, what we do ect.I don't however want it too busy, simple pictures and description of service.company colours and logo. I require simple one sided business cards toonumber, web address and logowinner will receive a request to design around 5 different double sided a5 flyers too, each with all our services on one side and the other primarily for one service we have provided locally with a spacve to put the house number down.REPAIRSROOFLINEFLAT ROOFS PITCHED ROOFSSYNTHETIC ROOFSUP TO 50 YEARS WARRANTY AVAILABLERANKED THE #1 FLAT ROOFER IN THE UK OUT OF 787 REGISTERED FLAT ROOFING COMPANIESRANKED THE #10 ROOFING COMPANY IN THE UK OUT OF 1976 REGISTERED SPECIALIST ROOFING COMPANIESBOTH FOR COST, CUSTOMER SERVICE AND QUALITY WITH 5 STAR REVIEWSGUARANTEED TO FIND AND FIX A LEAKAPPROVED INSTALLERSAWARD WINNINGTIME SERVED FIXED PRICES

Target Market(s)

homeowners

Colors

Designer to choose only greyscale colors for use in the design.

Requirements
Must have
• contact details
• pictures of my work
• clear and simple

```html
<!DOCTYPE html>
<html lang="en">
<head>
<meta charset="utf-8">
<title>Bramblegate Crest Roofing – Flyer</title>
<link href="https://fonts.googleapis.com/css2?family=Roboto:wght@400;500;700;900&display=swap" rel="stylesheet">
<style>
  :root{
    --page:#ffffff;
    --ink:#111111;
    --ink-soft:#3a3a3a;
    --grey-dark:#4a4a4a;
    --grey-mid:#6e6e6e;
    --grey-light:#b9b9b9;
    --grey-pale:#e6e6e6;
    --white:#ffffff;
  }
  *{box-sizing:border-box;margin:0;padding:0}
  html,body{width:1200px;height:1200px;overflow:hidden;background:var(--page)}
  body{font-family:"Roboto",Arial,sans-serif;color:var(--ink)}
  .flyer{
    position:absolute;left:222px;top:64px;width:757px;height:1072px;overflow:hidden;
    background:linear-gradient(180deg,#8d8d8d 0%,#d2d2d2 18%,#f4f4f4 38%,#ffffff 55%,#f2f2f2 80%,#9a9a9a 100%);
  }
  .photo{
    position:absolute;border-radius:50%;border:5px solid var(--white);
    box-shadow:0 6px 16px rgba(0,0,0,.45);
  }
  .photo--cottage{left:-22px;top:-6px;width:288px;height:288px;background:linear-gradient(160deg,#9b9b9b,#5d5d5d 60%,#7a7a7a)}
  .photo--gable{left:226px;top:-6px;width:304px;height:304px;background:linear-gradient(170deg,#cfcfcf 0%,#8a8a8a 45%,#5a5a5a 100%)}
  .photo--chimney{left:502px;top:182px;width:264px;height:264px;background:linear-gradient(175deg,#c8c8c8 0%,#9a9a9a 40%,#4e4e4e 100%)}
  .award-badge{
    position:absolute;left:608px;top:36px;width:118px;height:118px;border-radius:50%;
    background:var(--grey-dark);border:4px solid var(--grey-pale);box-shadow:0 0 0 2px var(--grey-dark);
  }
  .brand{
    position:absolute;left:74px;top:374px;width:430px;
    font-weight:900;color:var(--ink-soft);line-height:1;letter-spacing:1px;text-transform:uppercase;
  }
  .brand__line{display:block;font-size:42px;height:44px}
  .services{position:absolute;left:56px;list-style:none;font-weight:700;color:var(--ink-soft);font-size:26px}
  .services li{height:37.6px;line-height:37.6px}
  .services li::before{content:"•";margin-right:8px}
  .services--main{top:526px}
  .services--trust{top:800px}
  .services--trust li{height:auto;line-height:36px}
  .services--trust .indent{display:block;padding-left:22px}
  .guarantee-band{
    position:absolute;left:0;top:750px;width:420px;height:44px;
    background:linear-gradient(90deg,var(--grey-dark) 0%,var(--grey-mid) 70%,rgba(110,110,110,0) 100%);
    color:var(--white);font-weight:900;font-size:36px;line-height:44px;padding-left:62px;letter-spacing:.5px;
  }
  .rankings{
    position:absolute;left:446px;top:494px;width:330px;height:330px;border-radius:50%;
    background:radial-gradient(circle at 40% 35%,#7c7c7c,#5a5a5a 70%,#3e3e3e);
    border:5px solid var(--grey-pale);box-shadow:0 6px 18px rgba(0,0,0,.5);
  }
  .rankings__text{
    position:absolute;left:40px;top:50px;width:280px;transform:rotate(12deg);transform-origin:0 0;
    color:var(--white);text-align:center;font-weight:700;
  }
  .rank-title{font-size:33px;line-height:1}
  .rank-sub{font-size:27px;color:var(--grey-light);line-height:1}
  .rank-note{font-size:11px;line-height:1.2;margin-bottom:8px}
  .footnote{position:absolute;right:52px;top:882px;font-size:9px;font-weight:500;color:var(--grey-mid)}
  .reviews{position:absolute;right:52px;top:898px;font-size:23px;font-weight:500;color:var(--ink)}
  .call{position:absolute;left:54px;right:46px;top:938px;font-size:49px;font-weight:400;color:var(--ink);white-space:nowrap;text-align:right}
  .call strong{font-weight:900}
  .web{position:absolute;left:30px;right:46px;top:1000px;font-size:28px;font-weight:900;color:var(--white);text-align:right;letter-spacing:.4px}
</style>
</head>
<body>
  <main class="flyer">
    <div class="photo photo--cottage" role="img" aria-label="Photo of a finished slate roof on a pebble-dashed cottage"></div>
    <div class="photo photo--gable" role="img" aria-label="Photo of a brick gable end with new roof verge and window"></div>
    <div class="photo photo--chimney" role="img" aria-label="Photo of a restored brick chimney stack with pots"></div>
    <div class="award-badge" role="img" aria-label="Certificate of excellence badge"></div>

    <h1 class="brand">
      <span class="brand__line">Bramblegate</span>
      <span class="brand__line">Crest</span>
      <span class="brand__line">Roofing</span>
    </h1>

    <ul class="services services--main">
      <li>Roofline Repairs</li>
      <li>Flat Roofs</li>
      <li>Pitched Roofs</li>
      <li>Synthetic Roofs</li>
      <li>Up To 50 Year Warranty</li>
      <li>Leaks - Found &amp; Fixed</li>
    </ul>
    <div class="guarantee-band">GUARANTEED</div>
    <ul class="services services--trust">
      <li>Approved, time-served,<span class="indent">award-winning installers</span></li>
      <li>Fixed Prices</li>
    </ul>

    <div class="rankings">
      <div class="rankings__text">
        <div class="rank-title">Ranked #1</div>
        <div class="rank-sub">UK Flat Roofer</div>
        <div class="rank-note">(of 787 Registered Flat Roofing Companies)*</div>
        <div class="rank-title">Ranked #10</div>
        <div class="rank-sub">UK Roofing<br>Company</div>
        <div class="rank-note">(out of 1976 registered<br>specialist roofing companies)*</div>
      </div>
    </div>

    <p class="footnote">*for Cost, Customer Service and Quality</p>
    <p class="reviews">Check our 5***** Star Reviews online</p>
    <p class="call">Call Now <strong>07700900461</strong></p>
    <p class="web">www.bramblegatecrestroofing.com</p>
  </main>
</body>
</html>
```